Chauffeur Car Driver Needing a design with/without logo for business cards

I'm a chauffeur car driver in Melbourne Australia. I have an extensive list of personal customers and need to provide a professional business card to new customers.
My business name is 'RidgeMark'.
I offer a personalised service to customer who need a transport alternative to taxis. I don't want it to look too 'upmarket' as i don't want it to seem too expensive or only for special occasions. The majority of my clients are business professionals who use me for airport transfers.
I definitely don't want the card/logo to have an image of a car/road etc. I prefer something abstract. A 'pencil-line'-type font will grab my attention but not absolutely necessary. Not too 'digital' or 'ultra - modern' looking.
I need the card to display the following information
Ridge Mark - main logo/text
Chauffeur Cars - sub text
Bruno Fellisar
0498 271 536
bookings@RidgeMark.com.au
I would like the focus to be on 'RidgeMark' with everything else smaller.
Look forward to seeing ideas!!!!
Target Market(s)
Business Corporate Professionals
Industry/Entity Type
Airport
Requirements
Nice to have
- Pencil line type font
Should not have
- Images of cars, road, tyres, steering wheel etc.

```html
<!DOCTYPE html>
<html lang="en">
<head>
<meta charset="utf-8">
<title>RidgeMark Chauffeur Cars – Business Card</title>
<link rel="stylesheet" href="https://fonts.googleapis.com/css2?family=Yellowtail&family=Sue+Ellen+Francisco&display=swap">
<style>
  :root {
    --backdrop: #ececea;
    --card: #ffffff;
    --brand-red: #a52424;
    --ink: #1a1a1a;
    --card-shadow: rgba(0, 0, 0, 0.18);
  }
  html, body {
    margin: 0;
    padding: 0;
    width: 1200px;
    height: 724px;
    overflow: hidden;
    background: var(--backdrop);
  }
  .canvas {
    position: relative;
    width: 1200px;
    height: 724px;
  }
  .business-card {
    position: absolute;
    left: 100px;
    top: 92px;
    width: 1000px;
    height: 540px;
    background: var(--card);
    box-shadow: 0 4px 14px var(--card-shadow);
  }
  .accent-rule {
    position: absolute;
    left: 0;
    top: 232px;
    width: 560px;
    height: 4px;
    background: var(--brand-red);
  }
  .brand {
    position: absolute;
    right: 44px;
    top: 96px;
    text-align: right;
  }
  .brand-name {
    margin: 0;
    font-family: "Yellowtail", cursive;
    font-weight: 400;
    font-size: 112px;
    line-height: 1;
    color: var(--brand-red);
  }
  .brand-tagline {
    margin: 0;
    font-family: "Yellowtail", cursive;
    font-size: 40px;
    line-height: 1;
    color: var(--brand-red);
  }
  .contact {
    position: absolute;
    right: 44px;
    top: 300px;
    text-align: right;
  }
  .contact-name {
    margin: 0 0 14px;
    font-family: "Yellowtail", cursive;
    font-size: 52px;
    line-height: 1.1;
    color: var(--ink);
  }
  .contact-name .surname {
    color: var(--brand-red);
  }
  .contact-phone,
  .contact-email {
    margin: 0 0 12px;
    font-family: "Sue Ellen Francisco", cursive;
    line-height: 1.1;
    color: var(--ink);
  }
  .contact-phone { font-size: 40px; }
  .contact-email { font-size: 36px; }
</style>
</head>
<body>
  <main class="canvas">
    <article class="business-card">
      <div class="accent-rule"></div>
      <header class="brand">
        <h1 class="brand-name">RidgeMark</h1>
        <p class="brand-tagline">Chauffeur Cars</p>
      </header>
      <section class="contact">
        <p class="contact-name">Bruno <span class="surname">Fellisar</span></p>
        <p class="contact-phone">0498 271 536</p>
        <p class="contact-email">bookings@RidgeMark.com.au</p>
      </section>
    </article>
  </main>
</body>
</html>
```